KTR Football Academy Term 1 Certificate

Hello,
I require a certificate design which will be an improvement on previous designs attached.
The certificate must incorporate both logos and have the wording below.

Kestrel Track Rovers Football Academy
Certificate Of Participation
Presented to
______________________________________________________

For completing KTR Football Academy Term 1, 2024

```html
<!DOCTYPE html>
<html lang="en">
<head>
<meta charset="utf-8">
<title>KTR Football Academy – Certificate of Participation</title>
<link href="https://fonts.googleapis.com/css2?family=Montserrat:wght@500;600;800&family=Playfair+Display:wght@700;900&family=Allura&family=Oswald:wght@600&display=swap" rel="stylesheet">
<style>
  :root {
    --green: #7cc24a;
    --green-deep: #2f9a45;
    --ink: #2b2a2c;
    --grey: #6e6e70;
    --paper: #ffffff;
    --sky-top: #1f2b33;
    --sky-mid: #3e5561;
    --pitch: #2f7d3c;
  }
  html, body {
    margin: 0;
    padding: 0;
    width: 1200px;
    height: 848px;
    overflow: hidden;
    background: var(--paper);
  }
  .certificate {
    position: relative;
    width: 1200px;
    height: 848px;
    background: var(--paper);
    overflow: hidden;
    font-family: "Montserrat", Arial, sans-serif;
    color: var(--ink);
  }
  .side-panel {
    position: absolute;
    inset: 0;
    width: 1200px;
    height: 848px;
  }
  .academy-mark {
    position: absolute;
    left: 351px;
    top: 96px;
    width: 200px;
    display: flex;
    flex-direction: column;
    align-items: center;
    gap: 14px;
  }
  .academy-mark .dot {
    width: 70px;
    height: 70px;
    border-radius: 50%;
    background: var(--green);
  }
  .academy-mark .name {
    font-weight: 800;
    font-size: 52px;
    line-height: 1;
    color: var(--grey);
    letter-spacing: 0.02em;
  }
  .partner-mark {
    position: absolute;
    left: 772px;
    top: 92px;
    display: flex;
    align-items: center;
    gap: 10px;
  }
  .partner-mark .dot {
    width: 40px;
    height: 40px;
    border-radius: 50%;
    background: var(--green);
  }
  .partner-mark .name {
    font-weight: 800;
    font-size: 13px;
    line-height: 1.05;
    color: var(--green);
    text-transform: uppercase;
  }
  .academy-title {
    position: absolute;
    left: 0;
    width: 902px;
    top: 262px;
    text-align: center;
    font-weight: 800;
    font-size: 18px;
    letter-spacing: 0.01em;
    color: var(--ink);
    white-space: nowrap;
  }
  .academy-title .accent { color: var(--green); }
  .title-arc {
    position: absolute;
    left: 0;
    top: 0;
    width: 900px;
    height: 520px;
  }
  .title-arc text {
    font-family: "Playfair Display", Georgia, serif;
    font-weight: 900;
    font-size: 98px;
    fill: var(--ink);
  }
  .subtitle {
    position: absolute;
    left: 0;
    width: 882px;
    top: 456px;
    text-align: center;
    font-family: "Playfair Display", Georgia, serif;
    font-weight: 700;
    font-size: 31px;
    color: var(--ink);
    white-space: nowrap;
  }
  .subtitle .rule {
    display: inline-block;
    width: 26px;
    height: 4px;
    background: var(--ink);
    vertical-align: middle;
    margin: 0 12px;
  }
  .presented {
    position: absolute;
    left: 0;
    width: 890px;
    top: 545px;
    text-align: center;
    font-weight: 600;
    font-size: 21px;
    letter-spacing: 0.62em;
    color: var(--green);
  }
  .recipient {
    position: absolute;
    left: 134px;
    width: 611px;
    top: 572px;
    text-align: center;
    font-family: "Allura", cursive;
    font-size: 112px;
    line-height: 1;
    color: var(--ink);
    white-space: nowrap;
  }
  .name-line {
    position: absolute;
    left: 134px;
    top: 667px;
    width: 611px;
    height: 1.5px;
    background: var(--ink);
  }
  .completion {
    position: absolute;
    left: 0;
    width: 882px;
    top: 723px;
    text-align: center;
    line-height: 1;
  }
  .completion .lead {
    font-weight: 500;
    font-size: 16px;
    letter-spacing: 0.2em;
    display: block;
  }
  .completion .programme {
    font-weight: 800;
    font-size: 21px;
    display: block;
    margin-top: 4px;
  }
  .completion .term {
    font-family: "Oswald", "Arial Narrow", sans-serif;
    font-weight: 600;
    font-size: 38px;
    display: block;
    margin-top: 4px;
    letter-spacing: -0.01em;
  }
</style>
</head>
<body>
<main class="certificate">

  <svg class="side-panel" viewBox="0 0 1200 848" aria-hidden="false">
    <defs>
      <linearGradient id="team-photo-tone" x1="0" y1="0" x2="0" y2="1">
        <stop offset="0" stop-color="var(--sky-top)"/>
        <stop offset="0.22" stop-color="var(--sky-mid)"/>
        <stop offset="0.4" stop-color="var(--green-deep)"/>
        <stop offset="1" stop-color="var(--pitch)"/>
      </linearGradient>
    </defs>
    <polygon class="stripe-grey" points="990,0 1200,0 1200,848 771,848" fill="var(--grey)"/>
    <polygon class="stripe-green" points="993,0 1200,0 1200,848 800,848" fill="var(--green)"/>
    <polygon class="team-photo" points="996,0 1200,0 1200,848 823,848" fill="url(#team-photo-tone)" role="img" aria-label="Team photo of academy players in green kit standing with arms folded"/>
  </svg>

  <div class="academy-mark">
    <span class="dot"></span>
    <span class="name">KTR</span>
  </div>

  <div class="partner-mark">
    <span class="dot"></span>
    <span class="name">Kestrel<br>Track<br>Rovers</span>
  </div>

  <h1 class="academy-title"><span class="accent">KESTREL TRACK ROVERS</span> FOOTBALL ACADEMY</h1>

  <svg class="title-arc" viewBox="0 0 900 520">
    <path id="certificate-curve" d="M 130 470 Q 441 362 752 478" fill="none"/>
    <text><textPath href="#certificate-curve" startOffset="50%" text-anchor="middle" textLength="630" lengthAdjust="spacing">CERTIFICATE</textPath></text>
  </svg>

  <h2 class="subtitle"><span class="rule"></span>OF PARTICIPATION<span class="rule"></span></h2>

  <p class="presented" style="margin:0">PRESENTED TO</p>

  <p class="recipient" style="margin:0">Your Name</p>
  <div class="name-line"></div>

  <p class="completion" style="margin:0">
    <span class="lead">FOR COMPLETING</span>
    <span class="programme">KTR FOOTBALL ACADEMY</span>
    <span class="term">TERM 1, 2024</span>
  </p>

</main>
</body>
</html>
```